KEV.PRO- Darren Holcombe Fitness- needs a clever business card using the logo, name, info, contact

I need a business card designed for my Online Personal Training company called KEV.PRO, abbreviation for Darren Holcombe Fitness. My company focuses on coaching in personal health and personal growth to unleash your greatest potential. I would like to see designs that use my color scheme of a redish-orange (C:0,M:84,Y:100,K:0), grey, white, black, and my company font is OSWALD. The final design should communicate some aspects of design, health, motivation, growth, in some way. The logo is very important to the company and can be displayed in any of the colors previously mentioned. Must include the company name, my website: www.kev-pro.example , my email: dan@kev-pro.example

Target Market(s)

Personal health, fitness, general public, those who lack knowledge, awareness, and confidence in personal health

Industry/Entity Type

Personal Trainer

Font styles to use
Other font styles liked:
• OSWALD. (Bold, Regular, Light)

Colors
f37122
ffffff
9d9d9d
000000

Requirements
Must have
• Must include the logo, company name, my website: www.kev-pro.example , my email: dan@kev-pro.example
Nice to have
• Variations of the colors scheme of a redish-orange (C:0,M:84,Y:100,K:0), grey, white, black. Logo, card, or text can be in any of these colors.
• Possible quote like "Take control of your personal health to unleash your greatest potential" or "Unleashing your greatness first begins with fitness of the body and mind"

```html
<!DOCTYPE html>
<html lang="en">
<head>
<meta charset="utf-8">
<title>KEV.PRO – Business Card</title>
<link href="https://fonts.googleapis.com/css2?family=Oswald:wght@300;400;500;700&display=swap" rel="stylesheet">
<style>
  :root {
    --orange: #f37122;
    --white: #ffffff;
    --paper: #fafafa;
    --grey: #9d9d9d;
    --text-grey: #777777;
    --ink: #1f1f1f;
    --panel-dark: #1a1a1a;
    --backdrop: #2b2b2b;
  }
  * { margin: 0; padding: 0; box-sizing: border-box; }
  html, body {
    width: 1200px; height: 1200px; overflow: hidden;
    background: var(--backdrop);
    font-family: "Oswald", sans-serif;
  }
  .canvas { position: relative; width: 1200px; height: 1200px; }

  .card { position: absolute; left: 132px; width: 916px; height: 523px; overflow: hidden; }

  /* Front */
  .card-front { top: 65px; background: var(--paper); }
  .front-rays {
    position: absolute; left: 158px; top: 0; width: 600px; height: 370px;
    background: linear-gradient(180deg, rgba(243,113,34,0.06), rgba(157,157,157,0.05));
    clip-path: polygon(50% 0, 100% 100%, 0 100%);
  }
  .brand-mark {
    position: absolute; left: 0; right: 0; top: 205px;
    display: flex; justify-content: center; align-items: center; gap: 14px;
  }
  .brand-mark .dot { width: 26px; height: 26px; border-radius: 50%; background: var(--orange); }
  .brand-mark .name { font-weight: 700; font-size: 60px; line-height: 1; color: var(--orange); letter-spacing: 1px; }
  .front-title {
    position: absolute; left: 0; right: 0; top: 292px; text-align: center;
    font-weight: 400; font-size: 52px; line-height: 1; color: var(--ink);
    text-transform: uppercase; letter-spacing: 0.5px;
  }
  .front-rule { position: absolute; left: 0; right: 0; top: 369px; height: 3px; background: var(--orange); }
  .contact-icons {
    position: absolute; left: 0; right: 0; top: 389px;
    display: flex; justify-content: center; gap: 12px;
  }
  .contact-icons .icon {
    width: 36px; height: 36px; border-radius: 50%; background: var(--panel-dark);
    display: flex; align-items: center; justify-content: center;
  }
  .contact-lines {
    position: absolute; left: 0; right: 0; top: 425px; text-align: center;
    font-weight: 300; font-size: 25px; line-height: 28px; color: var(--text-grey);
  }

  /* Back */
  .card-back { top: 609px; display: flex; }
  .back-light { position: relative; width: 458px; height: 100%; background: var(--paper); }
  .back-dark { position: relative; flex: 1; height: 100%; background: var(--panel-dark); }
  .back-web {
    position: absolute; left: 0; right: 0; top: 20px; text-align: center;
    font-weight: 300; font-size: 24px; color: var(--text-grey);
  }
  .back-figures {
    position: absolute; left: 30px; top: 60px; width: 410px; height: 463px;
    background: linear-gradient(180deg, rgba(157,157,157,0.12), rgba(157,157,157,0.22));
    clip-path: polygon(40% 0, 70% 0, 75% 50%, 100% 75%, 100% 100%, 0 100%, 10% 70%, 35% 50%);
  }
  .back-brand { position: absolute; left: 110px; top: 392px; color: var(--ink); }
  .back-brand .short { font-weight: 700; font-size: 76px; line-height: 1; letter-spacing: -0.5px; }
  .back-brand .long { font-weight: 400; font-size: 22px; line-height: 1; margin-top: 2px; text-transform: uppercase; letter-spacing: -0.3px; }

  .service { position: absolute; left: 27px; top: 312px; text-transform: uppercase; }
  .service .lead { font-weight: 300; font-size: 38px; line-height: 44px; color: var(--white); }
  .service .main { font-weight: 400; font-size: 58px; line-height: 62px; color: var(--white); }
  .service .accent { font-weight: 700; font-size: 70px; line-height: 72px; color: var(--orange); }
</style>
</head>
<body>
<main class="canvas">
  <section class="card card-front">
    <div class="front-rays" role="img" aria-label="Faint radiating light beams rising behind the brand"></div>
    <div class="brand-mark"><span class="dot"></span><span class="name">KEV.PRO</span></div>
    <h1 class="front-title">Darren Holcombe Fitness</h1>
    <div class="front-rule"></div>
    <div class="contact-icons">
      <span class="icon">
        <svg width="18" height="13" viewBox="0 0 18 13"><rect x="0.5" y="0.5" width="17" height="12" fill="#fff"/><path d="M1 1 L9 7 L17 1" fill="none" stroke="#1a1a1a" stroke-width="1.2"/></svg>
      </span>
      <span class="icon">
        <svg width="18" height="18" viewBox="0 0 18 18" fill="none" stroke="#fff" stroke-width="1.2"><circle cx="9" cy="9" r="7.5"/><ellipse cx="9" cy="9" rx="3.5" ry="7.5"/><line x1="1.5" y1="9" x2="16.5" y2="9"/><line x1="9" y1="1.5" x2="9" y2="16.5"/><line x1="3" y1="5" x2="15" y2="5"/><line x1="3" y1="13" x2="15" y2="13"/></svg>
      </span>
    </div>
    <div class="contact-lines">
      <p>dan@kev-pro.example</p>
      <p>www.kev-pro.example</p>
    </div>
  </section>

  <section class="card card-back">
    <div class="back-light">
      <p class="back-web">www.kev-pro.example</p>
      <div class="back-figures" role="img" aria-label="Faint grey silhouettes of people doing fitness exercises"></div>
      <div class="back-brand">
        <p class="short">KEV.PRO</p>
        <p class="long">Darren Holcombe.Fitness</p>
      </div>
    </div>
    <div class="back-dark">
      <div class="service">
        <p class="lead">Online</p>
        <p class="main">Personal</p>
        <p class="accent">Training</p>
      </div>
    </div>
  </section>
</main>
</body>
</html>
```